VAMU, an e-commerce website with a twist, providing consumer-to-consumer and business-to-consumer sa

I have only uploaded 10 wire-frame pages of the website. These pages have been chosen for the different lay-outs and should give an idea of what will be needed. There are many more that I won’t upload yet, I aim to choose a winner first then there will be a high possibility that the winner will get the chance to do the design work for these later.
The design I have in mind is to keep it clean and easy with no/minimal fancy fonts and hieroglyphics. The logo is white with an orange highlight on a solid background of black, please note that the logo is white on a black background and is not a black box with white lettering, trust that makes sense. I like the idea of the top part of the website being black all the way across. I don’t see the need for more than 3 colours in the actual base website (the pictures and adverts added by users will add other colours). Although orange is the highlight colour in the logo I am open to suggestions on this, so long as the highlight colour features throughout the site.

Website width is 1220px, all pages in the PDF are 1220px

Logo font is Rezlong

The company is going to be like tradlo, but much more focused on raising money for charity and humanitarian relief.

Target Market(s)

the modern era of smartphones and the sharing community

Industry/Entity Type

Business

Number of Pages Required

5+ page

Font styles to use
Sans Serif
Other font styles liked:
• rezlong

Colors
faa54b
f78f20
ffffff
000000
fbfbfb
f5f5f5

Requirements
Nice to have
• Although orange is the highlight colour in the logo I am open to suggestions on this, so long as the highlight colour features throughout the site.

```html
<!DOCTYPE html>
<html lang="en">
<head>
<meta charset="utf-8">
<title>VAMU – Home</title>
<link rel="stylesheet" href="https://fonts.googleapis.com/css2?family=Roboto:wght@400;500;700&display=swap">
<style>
:root{
  --orange:#f78f20;
  --white:#ffffff;
  --black:#000000;
  --topbar:#1b1c1d;
  --page:#2f3134;
  --panel:#35373a;
  --panel-border:#4b4d50;
  --field-border:#55575a;
  --text-soft:#c9cacc;
  --text-mute:#a9abad;
}
*{box-sizing:border-box;margin:0;padding:0}
html,body{width:1200px;height:900px;overflow:hidden;background:var(--page);font-family:'Roboto',sans-serif;color:var(--white)}
.site{position:relative;width:1200px;height:900px}

.utility-bar{position:absolute;left:0;top:0;width:1200px;height:36px;background:var(--topbar);border-bottom:1px solid #2a2b2d;display:flex;align-items:center;font-size:13px;color:var(--text-soft)}
.utility-bar .link{padding:0 24px;border-right:1px solid #3c3d3f;line-height:14px;display:flex;align-items:center;gap:6px}
.utility-bar .link:last-child{border-right:none}
.utility-bar .count{color:var(--orange)}
.utility-bar .strong{color:var(--white)}
.utility-bar .spacer{flex:1}

.masthead{position:absolute;left:0;top:36px;width:1200px;height:158px;background:linear-gradient(#000 0%,#141516 100%);border-bottom:1px solid #3a3b3d}
.brand{position:absolute;left:26px;top:26px;font-size:54px;font-weight:700;letter-spacing:1px;line-height:1;color:var(--white)}
.btn{position:absolute;top:107px;height:28px;font-size:13px;font-weight:700;display:flex;align-items:center;justify-content:center}
.btn-signup{left:26px;width:84px;background:var(--orange)}
.btn-signin{left:134px;width:81px;border:1px solid var(--orange);color:var(--orange)}
.header-tool{position:absolute;right:22px;display:flex;align-items:center;gap:7px;font-size:13px;font-weight:700}
.icon-box{width:27px;height:27px;border:1px solid #5a5b5d;background:#111;display:flex;align-items:center;justify-content:center}
.cart{top:24px}.wish{top:66px}
.account-row{position:absolute;right:22px;top:112px;display:flex;align-items:center;font-size:13px;font-weight:700}
.account-row .account{display:flex;align-items:center;gap:8px;padding-right:24px;border-right:1px solid #3c3d3f}
.account-row .recent{padding-left:24px;display:flex;align-items:center;gap:9px}
.account-row .term{font-weight:400;font-size:15px;color:var(--text-soft)}
.account-row .x{color:var(--orange);font-weight:400}

.video-tile{position:absolute;left:26px;width:364px;height:207px;border:1px solid var(--panel-border);background:#151617}
.video-tile .thumb{position:absolute;left:0;top:0;width:362px;height:177px;background:linear-gradient(#151617,#232425)}
.video-tile .play{position:absolute;left:162px;top:70px}
.video-tile .caption{position:absolute;left:0;bottom:0;width:100%;height:28px;background:#3a3c3f;font-size:13px;font-weight:700;padding-left:20px;line-height:28px}
.about{top:244px}.charity{top:475px}

.search-panel{position:absolute;left:419px;top:244px;width:365px;height:438px;background:var(--panel);border:1px solid var(--panel-border)}
.field{position:absolute;left:29px;width:265px;height:38px;border:1px solid var(--field-border);font-size:15px;font-weight:500;padding-left:15px;line-height:36px;color:var(--text-soft)}
.help{position:absolute;left:309px}
.divider{position:absolute;left:29px;top:169px;width:305px;height:1px;background:var(--field-border)}
.label{position:absolute;font-size:15px;font-weight:700;color:var(--text-soft)}
.price-box{position:absolute;top:199px;height:36px;border:1px solid var(--field-border);font-size:15px;font-weight:500;line-height:34px;text-align:center}
.price-box.active{background:#8c8d8f;border-color:#8c8d8f}
.range-value{position:absolute;top:266px;font-size:15px;font-weight:700}
.track{position:absolute;left:29px;top:305px;width:305px;height:2px;background:#6b6d70}
.track-fill{position:absolute;left:123px;top:304px;width:182px;height:4px;background:var(--white)}
.knob{position:absolute;left:297px;top:298px;width:16px;height:16px;border-radius:50%;background:#c4c5c7;border:2px solid #eee}
.btn-search{position:absolute;left:29px;top:369px;width:305px;height:39px;background:var(--orange);font-size:15px;font-weight:500;display:flex;align-items:center;justify-content:center}

.scroll-bar{position:absolute;left:812px;width:364px;height:22px;background:#34363a;border:1px solid #3f4144;display:flex;align-items:center;justify-content:center}
.item-card{position:absolute;left:812px;width:364px;height:107px;background:var(--panel);border:1px solid var(--panel-border)}
.item-card .photo{position:absolute;left:9px;top:8px;width:98px;height:89px;background:linear-gradient(#5d6f8c 0%,#c99a6a 45%,#3a332d 60%,#1f1c1a 100%)}
.item-card .title{position:absolute;left:118px;top:10px;font-size:15px;font-weight:700}
.item-card .desc{position:absolute;left:118px;top:37px;width:175px;font-size:12.5px;line-height:16px;color:var(--text-soft)}
.item-card .act{position:absolute;left:317px}

.feature-band{position:absolute;left:26px;top:728px;width:1164px;height:172px;background:linear-gradient(90deg,#1e2a33,#243545 60%,#2a3340);border:1px solid #3f4144}
</style>
</head>
<body>
<div class="site">

  <nav class="utility-bar">
    <span class="link">
      <svg width="14" height="14" viewBox="0 0 14 14" fill="none" stroke="#f78f20" stroke-width="1.3"><path d="M2 3h6M2 3v9h9V7"/><path d="M6 8l6-6 1 1-6 6H6z"/></svg>
      Notifications <span class="count">(0)</span>
    </span>
    <span class="link">News</span>
    <span class="link">List Item</span>
    <span class="spacer"></span>
    <span class="link">Contact Us</span>
    <span class="link strong">Help</span>
    <span class="link">Terms and Conditions</span>
    <span class="link" style="padding-right:46px">
      <svg width="13" height="13" viewBox="0 0 13 13" fill="none" stroke="#c9cacc" stroke-width="1.3"><circle cx="5.5" cy="5.5" r="4"/><path d="M8.5 8.5l3.5 3.5"/></svg>
      Search
    </span>
  </nav>

  <header class="masthead">
    <div class="brand">VAMU</div>
    <span class="btn btn-signup">SIGN UP</span>
    <span class="btn btn-signin">SIGN IN</span>

    <div class="header-tool cart">My Cart (0)
      <span class="icon-box"><svg width="14" height="14" viewBox="0 0 14 14" fill="none" stroke="#fff" stroke-width="1.2"><rect x="2" y="5" width="10" height="8"/><path d="M4.5 5V3.5a2.5 2.5 0 0 1 5 0V5"/></svg></span>
    </div>
    <div class="header-tool wish">My Wish List (0)
      <span class="icon-box"><svg width="14" height="14" viewBox="0 0 14 14" fill="none" stroke="#fff" stroke-width="1.2"><path d="M7 12L2 7a3 3 0 0 1 5-4 3 3 0 0 1 5 4z"/></svg></span>
    </div>
    <div class="account-row">
      <span class="account">
        <svg width="15" height="13" viewBox="0 0 15 13" fill="none" stroke="#fff" stroke-width="1.3"><circle cx="7.5" cy="4" r="3"/><path d="M1 12h13"/></svg>
        My Account
      </span>
      <span class="recent">My Recent Searches:
        <span class="term">Funny Bear</span><span class="x">x</span>
        <span class="term">Bubble gum</span><span class="x">x</span>
      </span>
    </div>
  </header>

  <div class="video-tile about">
    <div class="thumb" role="img" aria-label="Video still introducing VAMU"></div>
    <svg class="play" width="40" height="48" viewBox="0 0 40 48"><path d="M3 3l34 21L3 45z" fill="none" stroke="#fff" stroke-width="3"/></svg>
    <div class="caption">What It's About</div>
  </div>
  <div class="video-tile charity">
    <div class="thumb" role="img" aria-label="Video still about VAMU charity work"></div>
    <svg class="play" width="40" height="48" viewBox="0 0 40 48"><path d="M3 3l34 21L3 45z" fill="none" stroke="#fff" stroke-width="3"/></svg>
    <div class="caption">What VAMU Does For Charity</div>
  </div>

  <section class="search-panel">
    <div class="field" style="top:29px">Item</div>
    <svg class="help" style="top:36px" width="24" height="24" viewBox="0 0 24 24" fill="none" stroke="#ddd" stroke-width="1.5"><circle cx="12" cy="12" r="10.5"/><path d="M9 9.5a3 3 0 1 1 4 2.8c-.8.4-1 .9-1 1.7"/><circle cx="12" cy="17.5" r=".6" fill="#ddd"/></svg>
    <div class="field" style="top:97px">Location</div>
    <svg class="help" style="top:104px" width="24" height="24" viewBox="0 0 24 24" fill="none" stroke="#ddd" stroke-width="1.5"><circle cx="12" cy="12" r="10.5"/><path d="M9 9.5a3 3 0 1 1 4 2.8c-.8.4-1 .9-1 1.7"/><circle cx="12" cy="17.5" r=".6" fill="#ddd"/></svg>
    <div class="divider"></div>

    <span class="label" style="left:29px;top:207px">From</span>
    <span class="price-box" style="left:81px;width:66px">£ 100</span>
    <span class="label" style="left:236px;top:207px">To</span>
    <span class="price-box active" style="left:269px;width:64px">£ 250|</span>

    <span class="range-value" style="left:112px">£ 100</span>
    <span class="range-value" style="left:287px">£ 250</span>
    <div class="track"></div>
    <div class="track-fill"></div>
    <div class="knob"></div>
    <span class="label" style="left:29px;top:322px">£ 0</span>
    <span class="label" style="left:308px;top:322px">£ ~</span>

    <span class="btn-search">SEARCH ITEM</span>
  </section>

  <div class="scroll-bar" style="top:244px"><svg width="18" height="9" viewBox="0 0 18 9" fill="none" stroke="#777" stroke-width="1.3"><path d="M1 8l8-7 8 7"/></svg></div>

  <article class="item-card" style="top:278px">
    <div class="photo" role="img" aria-label="Item photo: hillside at sunset"></div>
    <div class="title">Item Title</div>
    <p class="desc">Cras quis nulla commodo, aliquam lectus sed, blandit augue.</p>
    <svg class="act" style="top:18px" width="26" height="26" viewBox="0 0 26 26" fill="none" stroke="#ddd" stroke-width="1.3"><circle cx="13" cy="13" r="11.5"/><rect x="8.5" y="11" width="9" height="7"/><path d="M10.5 11V9.5a2.5 2.5 0 0 1 5 0V11"/></svg>
    <svg class="act" style="top:62px" width="26" height="26" viewBox="0 0 26 26" fill="none" stroke="#ddd" stroke-width="1.3"><circle cx="13" cy="13" r="11.5"/><path d="M13 18l-4.5-4.5a2.6 2.6 0 0 1 4.5-3 2.6 2.6 0 0 1 4.5 3z"/></svg>
  </article>
  <article class="item-card" style="top:410px">
    <div class="photo" role="img" aria-label="Item photo: hillside at sunset"></div>
    <div class="title">Item Title</div>
    <p class="desc">Cras quis nulla commodo, aliquam lectus sed, blandit augue.</p>
    <svg class="act" style="top:18px" width="26" height="26" viewBox="0 0 26 26" fill="none" stroke="#ddd" stroke-width="1.3"><circle cx="13" cy="13" r="11.5"/><rect x="8.5" y="11" width="9" height="7"/><path d="M10.5 11V9.5a2.5 2.5 0 0 1 5 0V11"/></svg>
    <svg class="act" style="top:62px" width="26" height="26" viewBox="0 0 26 26" fill="none" stroke="#ddd" stroke-width="1.3"><circle cx="13" cy="13" r="11.5"/><path d="M13 18l-4.5-4.5a2.6 2.6 0 0 1 4.5-3 2.6 2.6 0 0 1 4.5 3z"/></svg>
  </article>
  <article class="item-card" style="top:543px">
    <div class="photo" role="img" aria-label="Item photo: hillside at sunset"></div>
    <div class="title">Item Title</div>
    <p class="desc">Cras quis nulla commodo, aliquam lectus sed, blandit augue.</p>
    <svg class="act" style="top:18px" width="26" height="26" viewBox="0 0 26 26" fill="none" stroke="#ddd" stroke-width="1.3"><circle cx="13" cy="13" r="11.5"/><rect x="8.5" y="11" width="9" height="7"/><path d="M10.5 11V9.5a2.5 2.5 0 0 1 5 0V11"/></svg>
    <svg class="act" style="top:62px" width="26" height="26" viewBox="0 0 26 26" fill="none" stroke="#ddd" stroke-width="1.3"><circle cx="13" cy="13" r="11.5"/><path d="M13 18l-4.5-4.5a2.6 2.6 0 0 1 4.5-3 2.6 2.6 0 0 1 4.5 3z"/></svg>
  </article>

  <div class="scroll-bar" style="top:660px"><svg width="18" height="9" viewBox="0 0 18 9" fill="none" stroke="#777" stroke-width="1.3"><path d="M1 1l8 7 8-7"/></svg></div>

  <div class="feature-band" role="img" aria-label="Featured banner photograph"></div>
</div>
</body>
</html>
```